Financial Dashboard UI design

We are building a financial dashboard for business management teams, and would like a futuristic and sophisticated design (light and dark themes).

There are a total of 3 screens (attached images: nemo1, nemo2, nemo3).
nemo1 image is comprised of 6 scorecards (attached image: scorecard)
This will also need a design.

So, I'm expecting 4 UI designs in total.

I've added some example UI for inspiration. (sample1 , sample2, sample3, sample4).

Thanks

```html
<!DOCTYPE html>
<html lang="en">
<head>
<meta charset="utf-8">
<title>2021 U.S Sales – Report</title>
<link href="https://fonts.googleapis.com/css2?family=Titillium+Web:wght@400;600;700&family=Open+Sans:wght@400;600&display=swap" rel="stylesheet">
<style>
  :root{
    --page:#120f26;
    --topbar:#1b1932;
    --panel:#181630;
    --field:#211e3d;
    --icon:#3b3863;
    --text:#ffffff;
    --muted:#cfcde0;
    --faint:#6b6890;
    --accent:#6a2ee0;
    --red:#f0364f;
    --green:#33c45c;
    --alert:#e4122c;
    --cyan:#2fb8f0;
    --pink:#e21ca8;
    --line:#221f3d;
  }
  *{box-sizing:border-box;margin:0;padding:0}
  html,body{width:1200px;height:725px;overflow:hidden;background:var(--page);color:var(--text);font-family:"Open Sans",sans-serif}
  .topbar{position:absolute;left:0;top:0;width:1200px;height:62px;background:var(--topbar)}
  .search-field{position:absolute;left:38px;top:14px;width:252px;height:34px;border-radius:17px;background:var(--field);display:flex;align-items:center;padding-left:19px;gap:9px;font-size:8px;color:var(--muted)}
  .tool{position:absolute;top:21px;width:20px;height:20px}
  .badge{position:absolute;top:-5px;right:-7px;width:13px;height:13px;border-radius:50%;font:600 6.5px/13px "Open Sans",sans-serif;text-align:center;color:#0f0c24}
  .badge.cyan{background:var(--cyan)}
  .badge.pink{background:var(--pink);color:#fff}
  .lang{position:absolute;left:926px;top:14px;width:89px;height:34px;border-radius:17px;background:var(--field);display:flex;align-items:center;padding-left:10px;gap:7px;font:700 7.5px "Titillium Web",sans-serif;letter-spacing:.2px}
  .avatar{position:absolute;left:1047px;top:15px;width:29px;height:30px;border-radius:4px;background:#d9d9d9}
  .user{position:absolute;left:1089px;top:19px;font-family:"Titillium Web",sans-serif}
  .user .name{font-size:7.5px;font-weight:700}
  .user .role{font-size:6px;color:var(--faint);margin-top:3px}
  .user-caret{position:absolute;left:1152px;top:27px}

  .panel{position:absolute;left:58px;top:101px;width:1083px;height:584px;border-radius:8px;background:var(--panel)}
  .title{position:absolute;left:26px;top:14px;font:700 24px "Titillium Web",sans-serif}
  .subtitle{position:absolute;left:27px;top:49px;font:600 10px "Titillium Web",sans-serif;color:var(--muted)}
  .tabs{position:absolute;left:0;top:106px;width:100%;height:16px;font:600 11.5px "Titillium Web",sans-serif}
  .tabs span{position:absolute;transform:translateX(-50%);white-space:nowrap}
  .tabs .active{color:var(--accent)}

  .sales-table{position:absolute;left:21px;top:165px;width:1035px}
  .row{display:grid;grid-template-columns:138px 86px 154px 72px 118px 86px 160px 32px 118px 48px;height:40.6px;align-items:center;border-bottom:1px solid var(--line)}
  .row.head{height:27px;font:700 9.5px "Titillium Web",sans-serif;border-bottom:1px solid #26233f}
  .row > span{display:flex;justify-content:center;white-space:nowrap}
  .row.body{font-size:10.5px}
  .muted{color:var(--muted)}
  .neg{color:var(--red)}
  .pos{color:var(--green)}
  .fc{color:var(--accent);font-family:"Titillium Web",sans-serif;font-weight:600}
  .bold{font-weight:600}
  .flag{display:inline-block;background:var(--alert);padding:0 10px;line-height:13px}
  .scrollbar{position:absolute;left:1061px;top:209px;width:5px;height:51px;border-radius:3px;background:var(--accent)}
</style>
</head>
<body>
  <header class="topbar">
    <div class="search-field">
      <svg width="14" height="14" viewBox="0 0 14 14" fill="none" stroke="#4a4775" stroke-width="1.5"><circle cx="8" cy="6" r="4.8"/><path d="M4.6 9.4 1 13"/></svg>
      Search here
    </div>
    <div class="tool" style="left:776px"><svg width="20" height="20" viewBox="0 0 20 20" fill="var(--icon)"><path d="M10 2a5 5 0 0 0-5 5v5l-2 2v1h14v-1l-2-2V7a5 5 0 0 0-5-5zm-2 14a2 2 0 0 0 4 0z"/></svg><span class="badge cyan">12</span></div>
    <div class="tool" style="left:810px"><svg width="20" height="20" viewBox="0 0 20 20" fill="var(--icon)"><rect x="3" y="7" width="14" height="4" rx="1"/><rect x="4" y="11" width="12" height="7" rx="1"/><rect x="9" y="6" width="2" height="12" fill="#1b1932"/></svg><span class="badge cyan">5</span></div>
    <div class="tool" style="left:843px"><svg width="20" height="20" viewBox="0 0 20 20"><circle cx="10" cy="11" r="7" fill="var(--icon)"/><path d="M6.5 11l2.5 2.5 4.5-5" stroke="#1b1932" stroke-width="1.8" fill="none"/></svg><span class="badge cyan">2</span></div>
    <div class="tool" style="left:876px"><svg width="20" height="20" viewBox="0 0 20 20" fill="var(--icon)"><rect x="2" y="7" width="16" height="11" rx="2"/><path d="M7 7V5h6v2" stroke="var(--icon)" stroke-width="1.6" fill="none"/></svg><span class="badge pink">!</span></div>
    <div class="lang">
      <svg width="14" height="14" viewBox="0 0 14 14"><defs><clipPath id="round"><circle cx="7" cy="7" r="7"/></clipPath></defs><g clip-path="url(#round)"><rect width="14" height="14" fill="#fff"/><rect y="0" width="14" height="2" fill="#d22f3c"/><rect y="4" width="14" height="2" fill="#d22f3c"/><rect y="8" width="14" height="2" fill="#d22f3c"/><rect y="12" width="14" height="2" fill="#d22f3c"/><rect width="7" height="7" fill="#2c3f91"/></g></svg>
      ENGLISH
      <svg width="7" height="4" viewBox="0 0 7 4"><path d="M0 0h7L3.5 4z" fill="var(--accent)"/></svg>
    </div>
    <div class="avatar" role="img" aria-label="User profile photo"></div>
    <div class="user"><div class="name">Alex Reed</div><div class="role">Super Admin</div></div>
    <svg class="user-caret" width="8" height="5" viewBox="0 0 8 5"><path d="M0 0h8L4 5z" fill="var(--accent)"/></svg>
  </header>

  <main class="panel">
    <h1 class="title">2021 U.S Sales</h1>
    <p class="subtitle">Page 1 / 107 (2886 records)</p>

    <nav class="tabs">
      <span class="active" style="left:76px">Report</span>
      <span style="left:156px">Charts</span>
      <span style="left:233px">Email</span>
      <span style="left:315px">Calender</span>
      <span style="left:419px">Notifications</span>
      <span style="left:528px">Stand-in</span>
      <span style="left:612px">Tasks</span>
      <span style="left:690px">Market</span>
      <span style="left:769px">News</span>
      <span style="left:839px">Search</span>
      <span style="left:918px">Glossary</span>
      <span style="left:1001px">Settings</span>
    </nav>

    <div class="sales-table">
      <div class="row head"><span>Style index</span><span>Country</span><span>Business Area</span><span>Actual</span><span>Play</span><span>Forecast</span><span>Total</span><span>right</span><span>IT Sub Area</span><span>Same</span></div>
      <div class="row body"><span class="bold">Adinistration</span><span class="muted">Germany</span><span class="muted">Distribution</span><span class="neg">3674.54</span><span class="bold">0</span><span class="fc">0</span><span class="pos">3674.54</span><span class="muted">NY</span><span class="bold">Adinistration</span><span class="muted">50700</span></div>
      <div class="row body"><span class="bold">Adinistration</span><span class="muted">Germany</span><span class="muted">Distribution</span><span class="neg">234.00</span><span class="bold">0</span><span class="fc">-650,036.34</span><span class="pos">234.00</span><span class="muted">NY</span><span class="bold">Adinistration</span><span class="muted">110</span></div>
      <div class="row body"><span class="bold">Adinistration</span><span class="muted">Germany</span><span class="muted">Distribution</span><span class="neg">234.00</span><span class="bold">0</span><span class="fc">2,456,221.55</span><span class="pos">234.00</span><span class="muted">NY</span><span class="bold">Adinistration</span><span class="muted">110</span></div>
      <div class="row body"><span class="bold">Adinistration</span><span class="muted">Germany</span><span class="muted">Distribution</span><span class="neg">432.23</span><span class="bold">0</span><span class="fc">1,672.45</span><span class="pos">432.23</span><span class="muted">NY</span><span class="bold">Adinistration</span><span class="muted">2345</span></div>
      <div class="row body"><span class="bold">Adinistration</span><span class="muted">Germany</span><span class="muted">Distribution</span><span class="neg">432.90</span><span class="bold">0</span><span class="fc">800,561.00</span><span class="pos">432.90</span><span class="muted">NY</span><span class="bold">Adinistration</span><span><span class="flag">-234</span></span></div>
      <div class="row body"><span class="bold">Adinistration</span><span class="muted">Germany</span><span class="muted">Distribution</span><span class="neg">323.94</span><span class="bold">0</span><span class="fc">245,662.32</span><span class="pos">323.94</span><span class="muted">NY</span><span class="bold">Adinistration</span><span><span class="flag">-678</span></span></div>
      <div class="row body"><span class="bold">Adinistration</span><span class="muted">Germany</span><span class="muted">Distribution</span><span class="neg">934.97</span><span class="bold">0</span><span class="fc">$ 998.45</span><span class="neg bold">-934.97</span><span class="muted">NY</span><span class="bold">Adinistration</span><span class="muted">679</span></div>
      <div class="row body" style="border-bottom:none"><span class="bold">Adinistration</span><span class="muted">Germany</span><span class="muted">Distribution</span><span class="neg">1283.93</span><span class="bold">0</span><span class="fc">$ 700.00</span><span class="pos">1283.93</span><span class="muted">NY</span><span class="bold">Adinistration</span><span class="muted">8974</span></div>
    </div>
    <div class="scrollbar"></div>
  </main>
</body>
</html>
```